Dorvelan Swimming & Athletics Center

We need Business Card for a Athletics center
The logo frome the Uploaded Files ( b card fimal)
Οn one side of card we need the logo of company the Contact and the website:
1. Address:(Limassol, Cyprus 12-14 Stavrinelou str,Ano Trimeni,P.C. 4832)

2.Phone number: (+357) 25-704263

3. Mail: info@dorvelanfit.example

3. Website: www.dorvelanfit.example

Οn the other side of the card we need to write the sport of the company:

1. Artistic Gymnastics
2. Swimming
3. Gym - Fitness
4. Programs
5. Dancing
5.Tennis

From the Uploaded Files you can get the logo.In a logo is behind the black color which can be removed from logo.

Υou can use that color you want.
.
Updates

Industry/Entity Type

Business

Font styles to use
Decorative

Colors
0555a3
ffcf3e
3176b5
0692cd
add136
f04a50
000000
cfcfcf
9d9d9d

Requirements
Should not have
• photos with faces
• photo fro the Website:www.dorvelanfit.example

```html
<!DOCTYPE html>
<html lang="en">
<head>
<meta charset="utf-8">
<title>Dorvelan Swimming &amp; Athletics Center – Business Card</title>
<link href="https://fonts.googleapis.com/css2?family=Montserrat:wght@400;500;700&display=swap" rel="stylesheet">
<style>
  :root {
    --backdrop: #cfd0d2;
    --paper: #ffffff;
    --ink: #1a1a1a;
    --night: #000000;
    --brand-blue: #0555a3;
    --brand-gold: #ffcf3e;
    --logo-gold: #f2ac1c;
    --ring-dark: #14182a;
    --muted: #3a3a3a;
  }
  * { margin: 0; padding: 0; box-sizing: border-box; }
  html, body { width: 1200px; height: 927px; overflow: hidden; }
  body {
    background: var(--backdrop);
    font-family: "Montserrat", Arial, sans-serif;
    position: relative;
  }
  .card {
    position: absolute;
    top: 107px;
    width: 408px;
    height: 712px;
    box-shadow: 6px 8px 10px rgba(0,0,0,0.35);
    text-align: center;
  }
  .card--front { left: 182px; background: var(--paper); color: var(--ink); }
  .card--back { left: 610px; background: var(--night); color: #fff; }

  .brand {
    position: absolute;
    left: 36px;
    top: 176px;
    transform: translateY(-50%);
    display: flex;
    align-items: center;
    gap: 14px;
  }
  .brand__name {
    font-weight: 700;
    font-size: 37px;
    letter-spacing: 1px;
    color: var(--logo-gold);
  }
  .brand__dot {
    width: 56px; height: 56px; border-radius: 50%;
    background: var(--ring-dark);
    border: 2px solid var(--logo-gold);
  }

  .person { position: absolute; left: 0; right: 0; top: 418px; }
  .person__name {
    font-weight: 500; font-size: 29px; color: var(--brand-blue); line-height: 34px;
  }
  .person__role { font-size: 18px; line-height: 22px; }
  .address { margin-top: 8px; font-size: 18px; line-height: 22px; }
  .icons {
    margin: 10px auto 0;
    display: flex; justify-content: center; gap: 12px;
  }
  .icons svg { width: 13px; height: 13px; }
  .contact { margin-top: 10px; font-size: 18px; line-height: 22.5px; letter-spacing: 0.3px; }
  .contact .accent { color: var(--brand-blue); font-weight: 500; }

  .emblem {
    position: absolute; left: 106px; top: 69px;
    width: 204px; height: 204px; border-radius: 50%;
    background: var(--ring-dark);
    border: 4px solid #f3e18a;
  }
  .emblem-name {
    position: absolute; left: 0; right: 0; top: 296px;
    font-weight: 700; font-size: 30px; letter-spacing: 2px; color: var(--logo-gold);
  }
  .sports {
    position: absolute; left: 0; right: 0; top: 473px;
    list-style: none; font-size: 18px; line-height: 22px; letter-spacing: 0.8px;
  }
  .site {
    position: absolute; left: 0; right: 0; top: 620px;
    font-size: 22px; letter-spacing: 0.8px;
  }
  .site .accent { color: var(--brand-gold); font-weight: 500; }
</style>
</head>
<body>
  <section class="card card--front">
    <div class="brand">
      <span class="brand__name">DORVELAN</span>
      <span class="brand__dot"></span>
    </div>
    <div class="person">
      <p class="person__name">Marek Hollins</p>
      <p class="person__role">Director</p>
      <p class="address">Limassol, Cyprus<br>12-14 Stavrinelou<br>str,Ano Trimeni,P.C. 4832</p>
      <div class="icons" aria-hidden="true">
        <svg viewBox="0 0 16 16"><path d="M4 1.5l2.5 3-1.5 1.5c.8 2 2.5 3.8 4.5 4.6l1.5-1.5 3 2.4-1.6 2.5C7.5 13.5 2.5 8.5 1.5 3.2z" fill="none" stroke="#0555a3" stroke-width="1.5" stroke-linejoin="round"/></svg>
        <svg viewBox="0 0 16 16"><rect x="1.5" y="3.5" width="13" height="9" fill="none" stroke="#0555a3" stroke-width="1.5"/><path d="M1.5 3.5l6.5 5 6.5-5" fill="none" stroke="#0555a3" stroke-width="1.5"/></svg>
        <svg viewBox="0 0 16 16"><g fill="none" stroke="#0555a3" stroke-width="1.2"><circle cx="8" cy="8" r="6.5"/><ellipse cx="8" cy="8" rx="3" ry="6.5"/><path d="M1.5 8h13M2.5 5h11M2.5 11h11"/></g></svg>
      </div>
      <p class="contact">(+357) 25-704263<br>info@dorvelanfit.example<br>www.<span class="accent">dorvelanfit</span>.example</p>
    </div>
  </section>

  <section class="card card--back">
    <div class="emblem"></div>
    <p class="emblem-name">DORVELAN</p>
    <ul class="sports">
      <li>ARTISTIC GYMNASTICS</li>
      <li>SWIMMING</li>
      <li>GYM - FITNESS</li>
      <li>PROGRAMS</li>
      <li>DANCING</li>
      <li>TENNIS</li>
    </ul>
    <p class="site">www.<span class="accent">dorvelanfit</span>.example</p>
  </section>
</body>
</html>
```